THE TALL COPPER ATLAS OF PORTS

subtitle: AN INTRO TO SEARCH ENGINE OPTIMIZATION
background: white
dimensions: 1562x2500

Target Market(s)

Marketing professionals

Industry/Entity Type

Digital Marketing

Font styles to use
Sans Serif

Colors
ffffff
1b1b1b
3176b5

Requirements
Should not have
• Images or graphics

```html
<!DOCTYPE html>
<html lang="en">
<head>
<meta charset="utf-8">
<title>The Tall Copper Atlas of Ports — Cover</title>
<link rel="stylesheet" href="https://fonts.googleapis.com/css2?family=League+Spartan:wght@500;600;700&display=swap">
<style>
  :root {
    --paper: #ffffff;
    --ink: #1b1b1b;
    --accent: #3176b5;
    --backdrop: #ececec;
  }
  html, body {
    margin: 0;
    width: 1200px;
    height: 1200px;
    overflow: hidden;
    background: var(--backdrop);
  }
  .stage {
    width: 1200px;
    height: 1200px;
    display: flex;
    align-items: center;
    justify-content: center;
  }
  .book-cover {
    width: 750px;
    height: 1200px;
    background: var(--paper);
    display: block;
  }
  .cover-type {
    font-family: "League Spartan", "Futura", sans-serif;
    text-transform: uppercase;
  }
  .ink { fill: var(--ink); }
  .accent { fill: var(--accent); }
  .series-name { font-size: 27px; font-weight: 600; letter-spacing: 6px; }
  .title-word { font-weight: 600; }
  .title-article { font-size: 125px; letter-spacing: 4px; }
  .title-major { font-size: 200px; letter-spacing: 6px; }
  .title-colour { font-size: 112px; letter-spacing: 3px; }
  .title-small { font-size: 62px; letter-spacing: 6px; }
  .title-link { font-size: 110px; letter-spacing: 2px; }
  .title-focus { font-size: 168px; letter-spacing: 4px; }
  .subtitle { font-size: 27px; font-weight: 600; letter-spacing: 5px; }
  .author-name { font-size: 86px; font-weight: 600; letter-spacing: 4px; }
</style>
</head>
<body>
<main class="stage">
  <svg class="book-cover cover-type" viewBox="0 0 804 1285" xmlns="http://www.w3.org/2000/svg" aria-label="Book cover: The Tall Copper Atlas of Ports">
    <g text-anchor="middle" dominant-baseline="central">
      <text class="series-name ink" transform="translate(195 267) rotate(-44)">Name of the Series</text>

      <text class="title-word title-article accent" transform="translate(188 378) rotate(-45)">The</text>
      <text class="title-word title-major ink" transform="translate(343 410) rotate(-45)">Tall</text>
      <text class="title-word title-colour accent" transform="translate(418 500) rotate(-45)">Copper</text>
      <text class="title-word title-small ink" transform="translate(612 535) rotate(45)">Atlas</text>
      <text class="title-word title-link accent" transform="translate(583 640) rotate(-45)">Of</text>
      <text class="title-word title-focus ink" transform="translate(548 845) rotate(45)">Ports</text>

      <text class="subtitle ink" transform="translate(308 755) rotate(45)">An <tspan class="accent">Intro</tspan> to</text>
      <text class="subtitle ink" transform="translate(413 920) rotate(45)">Search Engine Optimization</text>

      <text class="author-name accent" transform="translate(238 835) rotate(45)">Name</text>
      <text class="author-name accent" transform="translate(228 945) rotate(45)">Author</text>
    </g>
  </svg>
</main>
</body>
</html>
```